依頼詳細
概要、特徴にも書いたように、今回、分離発注に向けた営業用のチラシを作成して頂きたいです。

・すでに既存で新規顧客獲得用のパンフレット(高難度松浦工業)とチラシ(HARUKAZE)があり、今回は、それらに追加で挟む “分離発注を目的としたチラシ” の依頼となります。

※既存(高難度パンフレット)(添付資料1、2)
+
既存(HARUKAZE)(添付資料3)
+
“分離発注を目的としたチラシ”

既存の3つのチラシ(※添付資料1.2.3)と一緒に挟んで、配布したいので

流れを理解して作成していただけたら幸いです。

・流れ、
株式会社松浦工業は、高難度の足場を専門で営業しています。

また、その職人で構成されている、HARUKAZEというワンランク上の足場サービスも運営しています。(住人さんや近隣様、などへの配慮、最高のサービスを提供するブランド)
(HARUKAZEにもホームページがございます。)

安全には、費用がかかります。
人の命は尊いです。
工事は足場から始まり、足場で終わります。
そして、業者みんなが使う足場です。

弊社の売りを武器として運営し維持して行くためには、無駄な予算を削り、その予算を安心できる工事に生かす。

そして見た目も美しい職人で揃えている私たちと手を組みませんか。

。。。といった流れでイメージして作成して頂きたいです。

※弊社の売りに関しましては、添付した資料やホームページを確認して頂き、理解して頂きたいです。

・目的は、新規顧客の獲得ですが、分離発注の提案を載せたいです。

・新規顧客(ターゲット)→ビル建物のオーナー、元請業社、ゼネコンなど

・メリットとデメリットをまとめたマインドマップも添付しますので、必要であれば使ってください。
・他にも、ホームページもありますので、見ていただけたら、と思います。
・弊社は改修工事用の足場をメインで運営しております。
(居住者様や、近隣様、歩行者様からの安心や業者間、現場管理監督様とのコミュニケーションもとても大切にしております。)
・メリットのマインドマップの他にも、弊社を使うことでのメリットは、たくさんあります。
・どの立場から見ても美しい足場屋を目指しております。

記載項目
分離発注しませんか。

株式会社松浦工業
042−718−2964
https://matsuurakogyo-ashiba.example
↑↑
株式会社松浦工業(高難度専門の足場サービス)

https://harukaze-ashiba.example
↑↑
ワンランク上の足場サービス
HARUKAZE ホームページ

サイズ
A4
ページ数
両面
希望イメージ
シンプル 複雑
単色 カラフル
暗い 明るい
日常 高級
遊び心 厳粛
未来的 伝統的
女性的 男性的
希望する色
黄・オレンジ系、緑系、青系、既存チラシ(添付資料1.2.3)とのバランスで決めて頂きたい
納品ファイル
• 高解像度JPG (.jpg)
• イラストレーター形式 (.ai)
補足説明
↑↑
株式会社松浦工業(高難度専門の足場サービス)

↑↑
ワンランク上の足場サービス
HARUKAZE ホームページ

どちらも並行して運営しております!

ーーーーーーーーーーーーーーーーーーーーーーーーー

※多少の文字の変更などがしやすいように、アウトライン化されていないデータでも納品して頂きたいです。
みなさま、すばらしい作品をありがとうございます!

みなさまの作品を見て間違えに気づくことが出来ました。

一部、変更させてください!

3点あるのですが、

①1つ目は、このチラシを誰に当てた手紙にするのか、ですが、ターゲットは、
・ビルやマンション、学校など建物のオーナー様
・ビルやマンションの管理をしている管理会社様や、
・不動産会社様
・店舗、等の工事担当者様
に当てた手紙で作成して頂きたいです。

※よく考えたら工事会社が直接足場屋に依頼するのは、当前のことだと思いましたので、工事業者に当てるのはおかしい話だと気付いたので宜しくお願いいたします。

②見積もり依頼までの流れを盛り込んで頂きたいです。
流れ
平日の9:00〜17:00に
042−718−2964

に電話をして頂き、弊社の電話に出た物に、見積もりして欲しい物件のご住所をお聞かせください。

or

当社ホームページ問い合わせフォームのQRコード?
かURL??

で見積もり依頼のメッセージを頂けたら、

1週間以内にTerravue Mapsを元に概算でお見積もりして郵送させて頂きます。

※建物の改修工事が決まりましたら、弊社と工事業者様とで直接お打ち合わせして、施工します!
※安心、安全へのクオリティは、高品質をお約束しますので、安心してください。
※足場工事は、命の危険を伴う工事です。

。。。のような感じをうまく刺さる形で表現して頂きたいです。

③ターゲットに分離発注という意味を理解してもらえるのかも不安になってきたのですが、どうでしょうか。

このチラシに足場だけを分離発注しませんか?なのか、
直接発注しませんか、なのか、何か良い表現があればそれも考えていただけると幸いです。

分離発注でわかるから大丈夫だよ、であれば分離発注も構いません。
ただ僕が不安になっただけなので、
そこも何か良い案があればなーと思ったので、宜しくお願いいたします。

コロナで、大ダメージを受けてしまったので、これで、復活したいと考えております!

みなさま、どうか宜しくお願いいたします!

弊社の既存のパンフレットと一緒に配ることを踏まえてこの作品が一番良いのではないかと感じました。

この度は、本当にありがとうございました。
僕たちは、職人さん達の生活がもっと潤っていけるように、したいと考えております。
職人さん達の世界では土曜も仕事をすることが当たり前となっております。
しかし僕たちは価値の高い仕事を社会に広めていき、みんなが、より良い工事をしながら、生活も潤っていけるように考えております。
皆さんが作ってくれた作品から、僕たちは大きな気づきをゲットしました!
とても感謝しています。
本当に本当にありがとうございました。

```html
<!DOCTYPE html>
<html lang="ja">
<head>
<meta charset="utf-8">
<title>足場の窓口 チラシ</title>
<link href="https://fonts.googleapis.com/css2?family=Noto+Sans+JP:wght@400;500;700;900&display=swap" rel="stylesheet">
<style>
  :root{
    --blue:#1d63c8;
    --blue-dark:#0c4aa3;
    --blue-deep:#083b86;
    --blue-light:#e8f1fc;
    --yellow:#ffe33a;
    --orange:#f29200;
    --white:#ffffff;
    --ink:#1f2a3a;
    --grey:#c9d3df;
  }
  *{box-sizing:border-box;margin:0;padding:0}
  html,body{width:849px;height:1200px;overflow:hidden;background:#fff}
  body{font-family:"Noto Sans JP",sans-serif;color:var(--ink)}
  .flyer{position:relative;width:849px;height:1200px;overflow:hidden;background:var(--white)}
  .hero{position:absolute;left:0;top:0;width:849px;height:950px;
    background:linear-gradient(180deg,var(--blue) 0%,var(--blue-dark) 100%)}
  .ribbon{position:absolute;right:-62px;top:34px;width:240px;height:46px;transform:rotate(45deg);
    background:var(--orange);color:var(--white);font-weight:900;font-size:26px;letter-spacing:4px;
    display:flex;align-items:center;justify-content:center;box-shadow:0 2px 4px rgba(0,0,0,.25)}
  .targets{position:absolute;left:24px;top:16px;display:grid;grid-template-columns:176px 176px;gap:8px 10px}
  .target-tag{background:var(--white);color:var(--blue-dark);font-weight:900;font-size:19px;
    border-radius:6px;height:36px;display:flex;align-items:center;justify-content:center}
  .lead{position:absolute;left:24px;top:104px;color:var(--yellow);font-weight:900;font-size:38px;letter-spacing:1px}
  .title{position:absolute;left:20px;top:152px;color:var(--white);font-weight:900;font-size:86px;letter-spacing:4px;line-height:1}
  .phone{position:absolute;left:24px;top:252px;color:var(--white);font-weight:900;font-size:48px;
    display:flex;align-items:center;gap:8px;line-height:1}
  .phone svg{width:46px;height:40px}
  .hours{position:absolute;left:176px;top:306px;color:var(--white);font-weight:700;font-size:16px}
  .mascot{position:absolute;left:540px;top:70px;width:280px;height:570px;border-radius:140px 140px 20px 20px;
    background:linear-gradient(180deg,#3a7fd9 0%,#164c9e 100%);opacity:.9}
  .bubble{position:absolute;left:498px;top:22px;width:76px;height:190px;background:var(--white);border-radius:38px;
    writing-mode:vertical-rl;display:flex;align-items:center;justify-content:center;
    color:var(--blue-dark);font-weight:900;font-size:17px;line-height:1.35;padding:10px 0}
  .site-photo{position:absolute;left:30px;top:340px;width:200px;height:296px;border-radius:4px;
    background:linear-gradient(160deg,#cfd8e3 0%,#8ea3bb 60%,#6d7f95 100%)}
  .checklist{position:absolute;left:250px;top:490px;list-style:none}
  .checklist li{display:flex;align-items:center;gap:10px;color:var(--white);font-weight:900;font-size:25px;height:46px}
  .checklist svg{width:28px;height:28px;flex:none}
  .solve{position:absolute;left:0;top:652px;width:849px;text-align:center;color:var(--yellow);
    font-weight:900;font-size:44px;letter-spacing:2px}
  .worries{position:absolute;left:22px;top:720px;width:805px;display:grid;grid-template-columns:repeat(4,1fr);gap:10px}
  .worry{height:214px;display:flex;flex-direction:column;gap:6px}
  .worry-text{position:relative;background:var(--white);border-radius:10px;height:100px;padding:10px 12px;
    font-size:14px;font-weight:700;line-height:1.5;color:var(--ink)}
  .worry-text::after{content:"";position:absolute;left:50%;bottom:-10px;margin-left:-10px;
    border:10px solid transparent;border-bottom:0;border-top-color:var(--white)}
  .worry-person{flex:1;border-radius:8px;margin:8px 30px 0;background:linear-gradient(180deg,#a9c4e8 0%,#6f95c9 100%)}
  .contact{position:absolute;left:22px;top:962px;width:805px}
  .contact-head{background:var(--blue);color:var(--white);font-weight:900;font-size:22px;text-align:center;
    height:40px;display:flex;align-items:center;justify-content:center;border-radius:4px}
  .services{display:grid;grid-template-columns:repeat(3,1fr);gap:18px;margin-top:12px}
  .service-name{display:flex;align-items:center;gap:8px;color:var(--blue-dark);font-weight:900;font-size:20px;
    border-bottom:2px solid var(--blue);padding-bottom:4px}
  .service-name svg{width:30px;height:30px;flex:none}
  .service-text{font-size:12.5px;line-height:1.55;margin-top:6px;color:#333}
  .back-note{position:absolute;left:22px;top:1136px;width:805px;height:48px;border-radius:24px;background:var(--blue-dark);
    display:flex;align-items:center;justify-content:center;gap:10px;color:var(--yellow);font-weight:900;font-size:23px}
  .back-note .back-em{color:var(--white)}
</style>
</head>
<body>
<div class="flyer">
  <section class="hero">
    <div class="ribbon">保存版</div>
    <div class="targets">
      <div class="target-tag">ビルのオーナー様</div>
      <div class="target-tag">管理会社様</div>
      <div class="target-tag">不動産会社様</div>
      <div class="target-tag">学校法人様など</div>
    </div>
    <p class="lead">改修・修繕工事の時は</p>
    <h1 class="title">足場の窓口</h1>
    <p class="phone">
      <svg viewBox="0 0 46 40" aria-hidden="true"><path d="M6 14c0-6 8-9 17-9s17 3 17 9l-7 3-3-5c-4-1-10-1-14 0l-3 5z" fill="#fff"/><rect x="12" y="19" width="22" height="16" rx="3" fill="#fff"/><circle cx="23" cy="27" r="4" fill="#1d63c8"/></svg>
      042-718-2964
    </p>
    <p class="hours">平日 9:00～17:00</p>

    <div class="mascot" role="img" aria-label="ヘルメットをかぶった作業服姿の案内役キャラクターのイラスト"></div>
    <div class="bubble">まずは気軽に<br>聞いてみよう！</div>
    <div class="site-photo" role="img" aria-label="建物に組まれた足場の写真"></div>

    <ul class="checklist">
      <li><svg viewBox="0 0 28 28" aria-hidden="true"><rect x="1" y="1" width="26" height="26" rx="4" fill="#fff"/><path d="M7 14l5 5 9-10" stroke="#1d63c8" stroke-width="4" fill="none" stroke-linecap="round" stroke-linejoin="round"/></svg>修繕工事のお見積りを取る前に。</li>
      <li><svg viewBox="0 0 28 28" aria-hidden="true"><rect x="1" y="1" width="26" height="26" rx="4" fill="#fff"/><path d="M7 14l5 5 9-10" stroke="#1d63c8" stroke-width="4" fill="none" stroke-linecap="round" stroke-linejoin="round"/></svg>お見積りのチェックに最適。</li>
      <li><svg viewBox="0 0 28 28" aria-hidden="true"><rect x="1" y="1" width="26" height="26" rx="4" fill="#fff"/><path d="M7 14l5 5 9-10" stroke="#1d63c8" stroke-width="4" fill="none" stroke-linecap="round" stroke-linejoin="round"/></svg>プロの意見を聞いてみたい。</li>
    </ul>

    <h2 class="solve">こんなお悩みを全て解決！</h2>

    <div class="worries">
      <div class="worry">
        <p class="worry-text">業者に見積りを取ったが足場代が高かった。こんなにかかるの!?</p>
        <div class="worry-person" role="img" aria-label="悩む建物オーナーのイラスト"></div>
      </div>
      <div class="worry">
        <p class="worry-text">改修工事を考えているが業者の見積りが適正かわからない…</p>
        <div class="worry-person" role="img" aria-label="考え込む管理会社担当者のイラスト"></div>
      </div>
      <div class="worry">
        <p class="worry-text">品質は落としたくないが少しでも工事費用を安くする方法はない？</p>
        <div class="worry-person" role="img" aria-label="費用に悩む担当者のイラスト"></div>
      </div>
      <div class="worry">
        <p class="worry-text">専門知識がないから業者とのやりとりが大変だし面倒くさい。</p>
        <div class="worry-person" role="img" aria-label="困った表情の女性担当者のイラスト"></div>
      </div>
    </div>
  </section>

  <section class="contact">
    <h3 class="contact-head">まずはお気軽にお問い合わせください</h3>
    <div class="services">
      <div class="service">
        <p class="service-name"><svg viewBox="0 0 32 32" aria-hidden="true"><path d="M4 6h24v15H13l-6 6v-6H4z" fill="#1d63c8"/><circle cx="11" cy="13.5" r="2" fill="#fff"/><circle cx="16" cy="13.5" r="2" fill="#fff"/><circle cx="21" cy="13.5" r="2" fill="#fff"/></svg>お見積り前相談</p>
        <p class="service-text">業者に見積りを取る前に、足場代が適正かの目安となるお見積りをお出しします。比較検討にご活用ください。</p>
      </div>
      <div class="service">
        <p class="service-name"><svg viewBox="0 0 32 32" aria-hidden="true"><circle cx="13" cy="13" r="9" fill="none" stroke="#1d63c8" stroke-width="4"/><path d="M20 20l8 8" stroke="#1d63c8" stroke-width="5" stroke-linecap="round"/></svg>お見積りチェック</p>
        <p class="service-text">お手元の見積りが適正かをプロがチェック。無駄な費用を見つけ、安全を守りながら改善をご提案します。</p>
      </div>
      <div class="service">
        <p class="service-name"><svg viewBox="0 0 32 32" aria-hidden="true"><rect x="6" y="3" width="20" height="26" rx="3" fill="#1d63c8"/><rect x="9" y="6" width="14" height="6" fill="#fff"/><g fill="#fff"><rect x="9" y="15" width="4" height="4"/><rect x="14" y="15" width="4" height="4"/><rect x="19" y="15" width="4" height="4"/><rect x="9" y="21" width="4" height="4"/><rect x="14" y="21" width="4" height="4"/><rect x="19" y="21" width="4" height="4"/></g></svg>カンタン見積り</p>
        <p class="service-text">物件のご住所をお伝えいただくだけ。Terravue Mapsを元に概算見積りを作成し、1週間以内に郵送します。</p>
      </div>
    </div>
  </section>

  <p class="back-note"><span class="back-em">■</span>足場の窓口に頼むメリットは裏面をチェック！</p>
</div>
</body>
</html>
```